FC Quintel and Canvas flyer for our communications

1. Introduction:
FC Quintel is a dynamic and passionate amateur football club, consisting of approximately 600 members. We are looking to create a versatile Canvas poster template that can be used for various purposes, including promoting matches, announcing special events such as gala dinners or football tournaments, as well as for promoting our recruitment activities to schools.

2. Objective:
The aim of this project is to create an attractive and professional poster template that reflects the spirit of FC Quintel, while being easily adaptable for different types of communications. We want the template to convey the excitement, energy, and sense of belonging to our club, highlighting our primary colors (red and blue) as well as our logo.

3. Key Elements of the Template:
The template should include the following elements clearly and organized:

FC Quintel Logo: Ensure the club logo is displayed or even better a strong visual identification of the key element of the logo are easily recognizable on the poster.

Club Colors: Use the main FC Quintel colors (red and blue) dominantly to create a strong visual identification with the club.

Editable Spaces: Provide dedicated and editable spaces to include event-specific information such as date, time, venue, sponsor logos, and any other relevant content.

4. Layout and Composition:
The layout should be clean, balanced, and appealing, with clear visual hierarchy for each element. Ensure the template is flexible enough to accommodate different types of content while maintaining a consistent look.

5. Variants Options:
We would like to have different template variants, with slightly different layouts for match posters, special event announcements, and recruitment advertising posters. However, the core visual and key elements will remain the same.

6. Tone and Style:
The tone of the poster should be energetic, enthusiastic, and professional. Avoid overly cluttered elements and focus on simplicity and readability.

7. Format and Deliverables:
The template should be created in digital format (Canvas), with dimensions suitable for printing (e.g., A3 size) while also being compatible with digital media. Provide the template in an editable format (e.g., PSD or AI) as well as in final print-ready formats (PDF, JPG, PNG).

Target Market(s)

Fooball players, members of the club, parents of the kids of the clubs, sponsors

Industry/Entity Type

Football (soccer)

Font styles to use
Sans Serif

Colors
0054AA
0677BA
7BADD7
CADEEF
E8F1F8
0094D4
00A9DD
6FCCEA
C7EBF8
E9F6FB
EB3D1F
EC4F4E
F09395
F8D3D4
FCEDEE

Requirements
Must have
• Colors of the club

```html
<!DOCTYPE html>
<html lang="en">
<head>
<meta charset="utf-8">
<title>FC Quintel poster templates</title>
<link href="https://fonts.googleapis.com/css2?family=Alfa+Slab+One&family=Allura&family=Roboto+Condensed:wght@400;700&family=Roboto:wght@400;500&display=swap" rel="stylesheet">
<style>
:root{
  --red:#ec2434;
  --red-dark:#9c1024;
  --blue:#0a86cc;
  --blue-dark:#0054aa;
  --ink:#231f20;
  --paper:#ececec;
  --paper-light:#f8f8f8;
  --placeholder:#8e8e8e;
  --placeholder-text:#c8c8c8;
  --chip:#c4c4c4;
  --white:#ffffff;
}
*{margin:0;padding:0;box-sizing:border-box}
html,body{width:849px;height:1200px;overflow:hidden;background:var(--white)}
body{position:relative;font-family:"Roboto Condensed",sans-serif;color:var(--ink)}
.sheet{position:absolute;overflow:hidden;background:radial-gradient(ellipse at 50% 50%,var(--paper-light),var(--paper) 70%)}
.abs{position:absolute}
.slab{font-family:"Alfa Slab One",serif;line-height:1;white-space:nowrap}
.condensed{transform:scaleX(.8);transform-origin:center}
.grad-red{background:linear-gradient(#ef2b3c,var(--red-dark));-webkit-background-clip:text;background-clip:text;color:transparent}
.grad-blue{background:linear-gradient(var(--blue),var(--blue-dark));-webkit-background-clip:text;background-clip:text;color:transparent}
.outlined{filter:drop-shadow(1.5px 0 0 #fff) drop-shadow(-1.5px 0 0 #fff) drop-shadow(0 1.5px 0 #fff) drop-shadow(0 -1.5px 0 #fff) drop-shadow(1px 2px 1.5px rgba(0,0,0,.35))}
.centered{text-align:center}
.body-copy{font-size:7px;line-height:9.7px;text-align:center;color:var(--ink)}
.club-mark{display:flex;flex-direction:column;align-items:center;gap:4px}
.club-mark .disc{border-radius:50%;background:var(--white);border:2px solid var(--blue)}
.club-mark .name{font-family:"Roboto Condensed",sans-serif;font-weight:700;color:var(--blue-dark);white-space:nowrap}
.photo-slot{position:absolute;background:var(--placeholder);color:var(--placeholder-text);font-family:"Roboto",sans-serif;display:flex;align-items:center;justify-content:center}
.headline-dark{font-family:"Alfa Slab One",serif;color:var(--ink);text-align:center;font-size:23px;letter-spacing:.5px;white-space:nowrap;filter:drop-shadow(1px 0 0 #fff) drop-shadow(-1px 0 0 #fff) drop-shadow(0 1px 0 #fff) drop-shadow(0 -1px 0 #fff)}
.spaced-headline{display:flex;justify-content:space-between;font-family:"Alfa Slab One",serif;line-height:1;color:var(--red)}
.sponsors{position:absolute;left:0;right:0;text-align:center;color:var(--white)}
.sponsors .label{font-weight:700;font-size:8px}
.sponsors .row{display:flex;justify-content:center;gap:7px;margin-top:3px}
.sponsors .chip{width:19px;height:9px;background:var(--white);color:#777;font-size:2.6px;display:flex;align-items:center;justify-content:center}
.band{position:absolute;left:0;width:100%}
.content-chip{position:absolute;top:139px;width:46px;height:24px;background:var(--chip);border:1px solid #fff;color:#fff;font-size:5.5px;font-weight:700;display:flex;align-items:center;justify-content:center}
.contact{position:absolute;font-family:"Roboto",sans-serif;font-size:6.6px;display:flex;align-items:center;gap:5px;color:var(--ink);white-space:nowrap}
.contact svg{width:7px;height:7px}
.button{position:absolute;background:var(--blue);color:#fff;font-size:11px;display:flex;align-items:center;justify-content:center}
</style>
</head>
<body>

<!-- Wide banner -->
<section class="sheet banner" style="left:55px;top:57px;width:724px;height:179px">
  <svg class="abs" style="left:0;top:0" width="724" height="179" viewBox="0 0 724 179">
    <path d="M0 0H28Q70 90 28 179H0Z" fill="var(--blue)"/>
    <path d="M31 0Q85 90 33 179" fill="none" stroke="var(--blue)" stroke-width="1.2"/>
    <path d="M724 0H696Q654 90 696 179H724Z" fill="var(--red)"/>
    <path d="M693 0Q639 90 691 179" fill="none" stroke="var(--red)" stroke-width="1.2"/>
  </svg>
  <div class="abs club-mark" style="left:66px;top:40px;width:82px">
    <div class="disc" style="width:56px;height:56px"></div>
    <div class="name" style="font-size:17px">FC Quintel</div>
  </div>
  <div class="abs slab condensed centered grad-red outlined" style="left:140px;top:22px;width:300px;font-size:58px">DUMMY</div>
  <div class="abs slab condensed centered grad-red outlined" style="left:140px;top:74px;width:300px;font-size:58px">TEXT</div>
  <div class="abs slab condensed centered" style="left:376px;top:29px;width:318px;font-size:34px;color:var(--blue)">LOREM IPSUM</div>
  <p class="abs body-copy" style="left:425px;top:74px;width:212px;font-size:6.9px">Lorem Ipsum is simply dummy text of the printing and typesetting industry. Lorem Ipsum has been the industry's standard dummy text ever since the 1500s, when an unknown printer took a galley of type and scrambled it to make a type specimen book. It has survived not only five centuries, but also the leap into electronic typesetting,</p>
  <div class="content-chip" style="left:170px">content</div>
  <div class="content-chip" style="left:230px">content</div>
  <div class="content-chip" style="left:290px">content</div>
  <div class="content-chip" style="left:350px">content</div>
  <div class="contact" style="left:461px;top:146px">
    <svg viewBox="0 0 8 8"><rect width="8" height="8" fill="var(--ink)"/><path d="M1.5 2.5h5v3h-5z" fill="#fff"/><path d="M1.5 2.5L4 4.3 6.5 2.5" fill="none" stroke="var(--ink)" stroke-width=".6"/></svg>hello@quintelclub.org</div>
  <div class="contact" style="left:461px;top:159px">
    <svg viewBox="0 0 8 8"><rect width="8" height="8" fill="var(--ink)"/><path d="M2.2 1.6l1 1.3-.6.7q.6 1.2 1.8 1.8l.7-.6 1.3 1-.6.8Q3 6.4 1.6 2.3z" fill="#fff"/></svg>010 2030 4050</div>
  <div class="contact" style="left:556px;top:146px">
    <svg viewBox="0 0 8 8"><rect width="8" height="8" fill="var(--ink)"/><path d="M4 7L2 4a2 2 0 1 1 4 0z" fill="#fff"/><circle cx="4" cy="3.6" r=".7" fill="var(--ink)"/></svg>street in road - province</div>
  <div class="contact" style="left:556px;top:159px">
    <svg viewBox="0 0 8 8"><rect width="8" height="8" fill="var(--ink)"/><circle cx="4" cy="4" r="2.4" fill="none" stroke="#fff" stroke-width=".6"/><path d="M1.6 4h4.8M4 1.6v4.8" stroke="#fff" stroke-width=".5"/></svg>www.quintelclub.org</div>
</section>

<!-- Tall poster: gallery -->
<section class="sheet poster-gallery" style="left:55px;top:258px;width:349px;height:863px">
  <svg class="band" style="top:0" height="66" viewBox="0 0 349 66" preserveAspectRatio="none">
    <path d="M0 0H349V38Q175 78 0 38Z" fill="var(--red)"/>
    <path d="M5 22Q175 70 344 22" fill="none" stroke="#fff" stroke-width="1.3"/>
  </svg>
  <div class="abs club-mark" style="left:0;right:0;top:20px">
    <div class="disc" style="width:50px;height:50px"></div>
    <div class="name" style="font-size:14px">FC Quintel</div>
  </div>
  <div class="abs slab condensed centered grad-red outlined" style="left:-40px;width:429px;top:110px;font-size:68px">DUMMY</div>
  <div class="abs slab condensed centered grad-blue outlined" style="left:-40px;width:429px;top:166px;font-size:68px">TEXT</div>
  <div class="abs headline-dark" style="left:0;right:0;top:236px">HEDLINE LOREM</div>
  <div class="photo-slot" role="img" aria-label="Team photo" style="left:17px;top:266px;width:313px;height:126px;font-size:56px">image</div>
  <div class="abs headline-dark" style="left:0;right:0;top:408px">HEDLINE LOREM</div>
  <div class="photo-slot" role="img" aria-label="Match photo" style="left:17px;top:442px;width:97px;height:105px;font-size:20px">image</div>
  <div class="photo-slot" role="img" aria-label="Match photo" style="left:125px;top:442px;width:97px;height:105px;font-size:20px">image</div>
  <div class="photo-slot" role="img" aria-label="Match photo" style="left:233px;top:442px;width:97px;height:105px;font-size:20px">image</div>
  <div class="abs headline-dark" style="left:0;right:0;top:574px">HEDLINE LOREM</div>
  <div class="photo-slot" role="img" aria-label="Event photo" style="left:17px;top:609px;width:150px;height:159px;font-size:28px">image</div>
  <div class="photo-slot" role="img" aria-label="Event photo" style="left:180px;top:609px;width:150px;height:159px;font-size:28px">image</div>
  <svg class="band" style="bottom:0" height="66" viewBox="0 0 349 66" preserveAspectRatio="none">
    <path d="M0 28Q175 -10 349 28V66H0Z" fill="var(--blue)"/>
    <path d="M5 48Q175 8 344 48" fill="none" stroke="#fff" stroke-width="1.3"/>
  </svg>
  <div class="sponsors" style="top:832px">
    <div class="label">Sponcored by:</div>
    <div class="row"><span class="chip">Sponsor</span><span class="chip">Sponsor</span><span class="chip">Sponsor</span><span class="chip">Sponsor</span><span class="chip">Sponsor</span><span class="chip">Sponsor</span><span class="chip">Sponsor</span></div>
  </div>
</section>

<!-- Poster: announcement -->
<section class="sheet poster-announce" style="left:430px;top:258px;width:349px;height:492px">
  <svg class="band" style="top:0" height="66" viewBox="0 0 349 66" preserveAspectRatio="none">
    <path d="M0 0H349V38Q175 78 0 38Z" fill="var(--red)"/>
    <path d="M5 22Q175 70 344 22" fill="none" stroke="#fff" stroke-width="1.3"/>
  </svg>
  <div class="abs club-mark" style="left:0;right:0;top:20px">
    <div class="disc" style="width:50px;height:50px"></div>
    <div class="name" style="font-size:14px">FC Quintel</div>
  </div>
  <div class="abs spaced-headline" style="left:22px;right:10px;top:104px;font-size:42px"><span>H</span><span>E</span><span>A</span><span>D</span><span>L</span><span>I</span><span>N</span><span>E</span></div>
  <div class="abs slab condensed centered" style="left:-40px;width:429px;top:148px;font-size:50px;filter:drop-shadow(2px 3px 0 var(--ink))"><span style="color:var(--blue)">LOREM</span> <span style="color:var(--red)">IPSUM</span></div>
  <p class="abs body-copy" style="left:27px;top:214px;width:139px">Lorem Ipsum is simply dummy text of the printing and typesetting industry. Lorem Ipsum has been the industry's standard dummy text ever since the 1500s, when an unknown printer took a galley of type and scrambled it to make a type specimen book. It has survived not only five centuries, but also the leap into electronic typesetting,</p>
  <p class="abs body-copy" style="left:195px;top:214px;width:139px"><b>Lorem Ipsum</b> is simply dummy text of the printing and typesetting industry. Lorem Ipsum has been the industry's standard dummy text ever since the 1500s, when an unknown printer took a galley of type and scrambled it to make a type specimen book. It has survived not only five centuries, but also the leap into electronic typesetting,</p>
  <div class="abs" style="left:24px;top:380px;width:313px;height:40px;background:#fff;border-radius:5px"></div>
  <div class="abs centered" style="left:0;right:0;top:318px;font-family:'Allura',cursive;font-size:58px;line-height:1;color:var(--blue-dark);white-space:nowrap">Dummy text</div>
  <p class="abs body-copy" style="left:30px;top:385px;width:301px;font-size:6.6px;line-height:8.8px">Lorem Ipsum is simply dummy text of the printing and typesetting industry. Lorem Ipsum has been the industry's standard dummy text ever since the 1500s, when an unknown printer took a galley of type and scrambled it to make a type specimen book. It has survived not only five centuries, but also the leap into electronic typesetting,</p>
  <svg class="band" style="bottom:0" height="64" viewBox="0 0 349 64" preserveAspectRatio="none">
    <path d="M0 26Q175 -10 349 26V64H0Z" fill="var(--blue)"/>
    <path d="M5 40Q175 -2 344 40" fill="none" stroke="#fff" stroke-width="1.3"/>
  </svg>
  <div class="sponsors" style="top:456px">
    <div class="label">Sponcored by:</div>
    <div class="row"><span class="chip">Sponsor</span><span class="chip">Sponsor</span><span class="chip">Sponsor</span><span class="chip">Sponsor</span><span class="chip">Sponsor</span><span class="chip">Sponsor</span><span class="chip">Sponsor</span></div>
  </div>
</section>

<!-- Poster: recruitment -->
<section class="sheet poster-recruit" style="left:430px;top:772px;width:349px;height:349px">
  <svg class="band" style="top:0" height="62" viewBox="0 0 349 62" preserveAspectRatio="none">
    <path d="M0 0H349V34Q175 72 0 34Z" fill="var(--red)"/>
    <path d="M5 20Q175 62 344 20" fill="none" stroke="#fff" stroke-width="1.3"/>
  </svg>
  <div class="abs club-mark" style="left:0;right:0;top:14px">
    <div class="disc" style="width:44px;height:44px"></div>
    <div class="name" style="font-size:13px">FC Quintel</div>
  </div>
  <div class="abs slab condensed centered grad-red outlined" style="left:-40px;width:429px;top:80px;font-size:50px">HEADLINE</div>
  <p class="abs body-copy" style="left:22px;top:136px;width:305px;font-size:6.6px;line-height:9px">Lorem Ipsum is simply dummy text of the printing and typesetting industry. Lorem Ipsum has been the industry's standard dummy text ever since the 1500s, when an unknown printer took a galley of type and scrambled it to make a type specimen book. It has survived not only five centuries, but also the leap into electronic typesetting,</p>
  <div class="abs headline-dark condensed" style="left:27px;top:189px;width:140px;font-size:26px">LOREM</div>
  <div class="abs headline-dark condensed" style="left:179px;top:189px;width:140px;font-size:26px">IPSUM</div>
  <p class="abs body-copy" style="left:30px;top:222px;width:134px;font-size:4.6px;line-height:6.6px">Lorem Ipsum is simply dummy text of the printing and typesetting industry. Lorem Ipsum has been the industry's standard dummy text ever since the 1500s, when an unknown printer took a galley of type and scrambled it to make a type specimen book. It has survived not only five centuries, but also the leap into electronic typesetting,</p>
  <p class="abs body-copy" style="left:182px;top:222px;width:134px;font-size:4.6px;line-height:6.6px">Lorem Ipsum is simply dummy text of the printing and typesetting industry. Lorem Ipsum has been the industry's standard dummy text ever since the 1500s, when an unknown printer took a galley of type and scrambled it to make a type specimen book. It has survived not only five centuries, but also the leap into electronic</p>
  <div class="button" style="left:132px;top:265px;width:84px;height:19px">Lorem Ipsum</div>
  <svg class="band" style="bottom:0" height="50" viewBox="0 0 349 50" preserveAspectRatio="none">
    <path d="M0 22Q175 -8 349 22V50H0Z" fill="var(--blue)"/>
    <path d="M5 36Q175 0 344 36" fill="none" stroke="#fff" stroke-width="1.3"/>
  </svg>
  <div class="sponsors" style="top:321px">
    <div class="label">Sponcored by:</div>
    <div class="row"><span class="chip">Sponsor</span><span class="chip">Sponsor</span><span class="chip">Sponsor</span><span class="chip">Sponsor</span><span class="chip">Sponsor</span><span class="chip">Sponsor</span><span class="chip">Sponsor</span></div>
  </div>
</section>

</body>
</html>
```